Redesign company trifold brochure

We are rebranding our company in September and looking for a more professional design for our brochure.

What we do - providing interdisciplinary care for those supporting ill, elderly and special needs pets at home following the human hospice model of care - is very novel and our brochure is key in explaining it and our offerings.

We serve dogs and cats. Most of the animals are quite sick, elderly. I have many personal and stock photos we can use in the brochure. Please - no pictures of puppies and/or kittens.

The hard part is fitting the info and message into a clear and concise format.

It must be appealing both to pet owners and vets (who are our primary source of patients through referrals).

It should covey WARMTH, COMPASSION, PROFESSIONALISM, and EXPERTISE.

Please look at our website www.LarkvaleAnimalRest.com for more info

We have until now used maroon and copper for colors - to reflect the "sunset" of the pets life. BUT are now changing to Navy, Teal and White to reflect calm, trust and competence.

We will use the same logo recolored.

Existing brochure and new logo are attached.

PLEASE ask questions!!
Updates

We have a library of stock images you are welcome to use. All have been legally acquired and we have the right to use them. You DO NOT have to use them, just sending along in case you wish to. https://www.filecrate.example/sh/q7rmt2wzp40kdyh/BBR8Kxtz-Pqmn3vd7yHsLcWqe?dl=0

Our colors are NAVY, TEAL and WHITE. For your reference, the navy we use is 99/87/44/55 (CMYK) The Teal we use is 76/11/44/0 (CMYK) Thank you!

Designers -- pleaseuse pictures of older pets (no puppies or kittens). Below is a link to stock photos we own that would be appropriate for use in the brochure. https://www.filecrate.example/sh/k416f8m2twr5zqa/BBQe3LmxtvRVZWPgb8JTFYs_4m?dl=0 THANK YOU!

Designers -- I would VERY much like to include a photo of a pet in a wheel chair. I have personal photos as well as (purchased) stock photos for this purpose which can be found at http://lnkr.example/LARWC-Pets-in-Wheelchairs Thank you!!

Today is the last day! Many of you have submitted beautiful designs and others are rolling in. I am so appreciative of your time and energy!! Please do not let the deadline pass without YOUR very BEST entry being submitted!! Thank you! - Miriam & All of us at Larkvale Animal Rest & Comfort Care

Target Market(s)

Pet Owners and Veterinarians

Industry/Entity Type

Pet Care

Font styles to use
Serif

Colors
0455a3
33b8a4
ffffff

Requirements
Must have
• Our logo and information about our services. Pictures of pets. Our contact info. PLEASE NOTE: this is a 2 sided brochure. Please submit both inside and outside.
Should not have
• puppies, kittens - anything off message

```html
<!DOCTYPE html>
<html lang="en">
<head>
<meta charset="utf-8">
<title>Larkvale Animal Rest &amp; Comfort Care — Brochure</title>
<link rel="stylesheet" href="https://fonts.googleapis.com/css2?family=Montserrat:wght@400;500;600&family=Cormorant+Garamond:ital,wght@1,500;1,600&display=swap">
<style>
  :root{
    --navy:#13224a;
    --teal:#1fa89b;
    --teal-light:#33b8a4;
    --white:#ffffff;
    --ink:#1c2a6b;
    --stage:#6e7072;
    --photo-wood-a:#6b3a1f;
    --photo-wood-b:#a7683c;
    --photo-dog-a:#e2b47a;
    --photo-dog-b:#a8743f;
    --photo-cat-a:#f4f1ef;
    --photo-cat-b:#dcd3cf;
  }
  *{box-sizing:border-box;margin:0;padding:0}
  html,body{width:1200px;height:900px;overflow:hidden}
  body{background:var(--stage);font-family:"Montserrat",sans-serif;position:relative}
  .brochure{position:absolute;left:105px;top:65px;width:990px;height:770px;display:flex;box-shadow:0 10px 30px rgba(0,0,0,.35)}
  .panel{position:relative;width:330px;height:770px;background:var(--white);overflow:hidden}
  .panel + .panel{border-left:1px solid #e4e4e4}
  .panel svg.shape{position:absolute;left:0;top:0}

  /* team panel */
  .photo-wood{position:absolute;left:0;top:0;width:330px;height:210px;background:linear-gradient(135deg,var(--photo-wood-a),var(--photo-wood-b))}
  .photo-dog{position:absolute;left:28px;top:38px;width:150px;height:150px;border-radius:50%;border:5px solid var(--white);box-shadow:0 0 0 2px var(--teal);background:radial-gradient(circle at 50% 45%,var(--photo-dog-a),var(--photo-dog-b))}
  .team-list{position:absolute;left:30px;top:236px;list-style:none;color:var(--ink);font-size:12px;line-height:22px;font-style:italic;white-space:nowrap}
  .team-list li::before{content:"";display:inline-block;width:6px;height:6px;border-radius:50%;background:var(--ink);margin-right:10px;vertical-align:middle}
  .beliefs{position:absolute;left:26px;top:412px;width:285px;color:var(--white)}
  .beliefs h2{font-family:"Cormorant Garamond",serif;font-style:italic;font-weight:600;font-size:30px;margin-bottom:10px}
  .beliefs ul{list-style:none}
  .beliefs li{position:relative;padding-left:24px;font-size:12.5px;line-height:17px;margin-bottom:11px;font-style:italic}
  .beliefs li svg{position:absolute;left:0;top:2px}

  /* contact panel */
  .photo-strip{position:absolute;left:0;top:0;width:330px;height:170px;background:linear-gradient(160deg,var(--photo-wood-b),var(--photo-cat-b))}
  .contact{position:absolute;left:34px;top:220px;width:270px}
  .contact h2{font-family:"Cormorant Garamond",serif;font-style:italic;font-weight:600;color:var(--teal);font-size:28px;margin-bottom:6px}
  .contact .org{font-size:12px;color:var(--ink);margin-bottom:22px}
  .contact-row{display:flex;align-items:center;gap:12px;margin-bottom:18px;font-size:12.5px;color:var(--ink)}
  .contact-row svg{flex:none}

  /* cover panel */
  .photo-cat{position:absolute;left:0;top:0;width:330px;height:470px;background:linear-gradient(150deg,var(--photo-cat-a),var(--photo-cat-b) 70%,#e9c9c2)}
  .tagline{position:absolute;left:18px;top:34px;width:300px}
  .tagline span{display:table;white-space:nowrap;background:rgba(255,255,255,.92);color:var(--ink);font-size:21px;line-height:32px;padding:0 6px;margin-bottom:5px}
  .tagline-script{position:absolute;left:60px;top:232px;font-family:"Cormorant Garamond",serif;font-style:italic;font-weight:600;font-size:29px;line-height:30px;color:var(--navy)}
  .logo-seal{position:absolute;left:57px;top:370px;width:216px;height:216px;border-radius:50%;background:var(--navy);display:flex;align-items:center;justify-content:center;text-align:center}
  .logo-name{font-family:"Montserrat",sans-serif;font-weight:500;font-size:17px;line-height:23px;color:var(--white);width:150px}
  .social{position:absolute;left:0;top:620px;width:330px;display:flex;justify-content:center;gap:18px}
  .social i{width:34px;height:34px;border-radius:50%;background:var(--white);display:block}
  .handles{position:absolute;left:0;top:676px;width:330px;text-align:center;color:var(--navy);font-size:17px;line-height:26px;font-weight:500}
</style>
</head>
<body>
<main class="brochure">

  <section class="panel panel-team">
    <div class="photo-wood" role="img" aria-label="Photo of warm wooden background"></div>
    <svg class="shape" width="330" height="770" viewBox="0 0 330 770" aria-hidden="true">
      <path d="M0 150 C 90 215, 230 225, 330 200 L330 770 L0 770 Z" fill="var(--teal)"/>
      <path d="M0 185 C 100 240, 230 245, 330 225 L330 770 L0 770 Z" fill="var(--white)"/>
      <path d="M0 412 C 40 374, 180 364, 330 412 L330 770 L0 770 Z" fill="var(--teal)"/>
      <path d="M0 400 C 50 360, 190 352, 330 400" fill="none" stroke="var(--teal)" stroke-width="1.5"/>
    </svg>
    <div class="photo-dog" role="img" aria-label="Photo of an elderly golden retriever"></div>
    <ul class="team-list">
      <li>Interfaith Spiritual Advisor</li>
      <li>Certified Small Animal Massage Therapist</li>
      <li>Animal Care Specialists</li>
      <li>Hospice Assistants</li>
      <li>Client Care Coordinator</li>
    </ul>
    <div class="beliefs">
      <h2>We Believe</h2>
      <ul>
        <li><svg width="14" height="12" viewBox="0 0 14 12"><path d="M1 6 L5 10 L13 1" fill="none" stroke="#fff" stroke-width="2"/></svg>That animals are conscious beings, capable of thought, feeling, emotion and choice</li>
        <li><svg width="14" height="12" viewBox="0 0 14 12"><path d="M1 6 L5 10 L13 1" fill="none" stroke="#fff" stroke-width="2"/></svg>That each animal is an individual with his or her unique needs and wishes</li>
        <li><svg width="14" height="12" viewBox="0 0 14 12"><path d="M1 6 L5 10 L13 1" fill="none" stroke="#fff" stroke-width="2"/></svg>That all pets deserve to be pain-free</li>
        <li><svg width="14" height="12" viewBox="0 0 14 12"><path d="M1 6 L5 10 L13 1" fill="none" stroke="#fff" stroke-width="2"/></svg>That an interdisciplinary team is essential to addressing the needs of pets and their families through aging and illness</li>
        <li><svg width="14" height="12" viewBox="0 0 14 12"><path d="M1 6 L5 10 L13 1" fill="none" stroke="#fff" stroke-width="2"/></svg>That quality of life is subjective, best evaluated by the family who knows and loves the animal</li>
      </ul>
    </div>
  </section>

  <section class="panel panel-contact">
    <div class="photo-strip" role="img" aria-label="Photo of a resting senior pet"></div>
    <svg class="shape" width="330" height="770" viewBox="0 0 330 770" aria-hidden="true">
      <path d="M0 150 C 100 195, 230 200, 330 170 L330 200 C 230 225, 100 225, 0 185 Z" fill="var(--teal)"/>
      <path d="M0 660 C 110 620, 230 625, 330 650 L330 770 L0 770 Z" fill="var(--teal)"/>
    </svg>
    <div class="contact">
      <h2>Contact Us</h2>
      <p class="org">Larkvale Animal Rest &amp; Comfort Care</p>
      <div class="contact-row">
        <svg width="26" height="26" viewBox="0 0 26 26"><circle cx="13" cy="13" r="13" fill="var(--teal)"/><path d="M13 6 a5 5 0 0 1 5 5 c0 4-5 9-5 9 s-5-5-5-9 a5 5 0 0 1 5-5z" fill="#fff"/><circle cx="13" cy="11" r="2" fill="var(--teal)"/></svg>
        <span>PO Box 84, Larkvale, MA 01770</span>
      </div>
      <div class="contact-row">
        <svg width="26" height="26" viewBox="0 0 26 26"><circle cx="13" cy="13" r="13" fill="var(--teal)"/><path d="M8 7 l3 0 l1 4 l-2 1 a8 8 0 0 0 4 4 l1-2 l4 1 l0 3 a2 2 0 0 1-2 2 a12 12 0 0 1-11-11 a2 2 0 0 1 2-2z" fill="#fff"/></svg>
        <span>(555) 014-2290</span>
      </div>
      <div class="contact-row">
        <svg width="26" height="26" viewBox="0 0 26 26"><circle cx="13" cy="13" r="13" fill="var(--teal)"/><rect x="6" y="8" width="14" height="10" rx="1" fill="#fff"/><path d="M6 9 L13 14 L20 9" fill="none" stroke="var(--teal)" stroke-width="1.4"/></svg>
        <span>care@LarkvaleAnimalRest.com</span>
      </div>
      <div class="contact-row">
        <svg width="26" height="26" viewBox="0 0 26 26"><circle cx="13" cy="13" r="13" fill="var(--teal)"/><circle cx="13" cy="13" r="7" fill="none" stroke="#fff" stroke-width="1.5"/><path d="M6 13 H20 M13 6 C9 10 9 16 13 20 M13 6 C17 10 17 16 13 20" fill="none" stroke="#fff" stroke-width="1.2"/></svg>
        <span>www.LarkvaleAnimalRest.com</span>
      </div>
    </div>
  </section>

  <section class="panel panel-cover">
    <div class="photo-cat" role="img" aria-label="Photo of an elderly white cat resting"></div>
    <svg class="shape" width="330" height="770" viewBox="0 0 330 770" aria-hidden="true">
      <path d="M0 430 C 110 400, 240 380, 330 330 L330 770 L0 770 Z" fill="var(--teal)"/>
      <path d="M0 505 C 110 470, 240 440, 330 400 L330 470 C 240 500, 110 525, 0 545 Z" fill="var(--teal)"/>
      <path d="M0 402 C 110 372, 240 352, 330 302 L330 330 C 240 380, 110 400, 0 430 Z" fill="var(--navy)"/>
      <circle cx="165" cy="478" r="122" fill="none" stroke="var(--navy)" stroke-width="1.5"/>
    </svg>
    <div class="tagline">
      <span>Skilled Home Care for Ill,</span>
      <span>Elderly and Special</span>
      <span>Needs</span>
      <span>Animals</span>
    </div>
    <p class="tagline-script">Compassionate<br>&nbsp;&nbsp;Support for Families</p>
    <div class="logo-seal">
      <p class="logo-name">Larkvale Animal Rest &amp; Comfort Care</p>
    </div>
    <div class="social" aria-label="Social links"><i></i><i></i><i></i><i></i></div>
    <p class="handles">LarkvaleAnimalRest<br>LarkvaleRest</p>
  </section>

</main>
</body>
</html>
```